Realtor Ad for local community newspaper (Pell-Ledger)

Real Estate Agent, Relatively new to the industry and trying to get her name out into some local community newspapers. Looking to create an ad for a local newspaper. Please see pdf with the ad technical specs/details. Looking for ad size of 1/6 page and 1/8 page ad size. I have also added some stock logos and a copy of her current business card.

Target Market(s)

Anyone looking at buying or selling a home.

Industry/Entity Type

Real Estate Agent

Colors

Designer to choose colors to be used in the design.

Requirements
Must have
• Must have the VESTRAN ®, underneath or next to her name Nora Bastevin
• I would like to have her picture in the ad.
Should not have
• The mailing address does not need to be in the ad.
• The phone number 302.555.0162 does not need to be in the ad either.

```html
<!DOCTYPE html>
<html lang="en">
<head>
<meta charset="utf-8">
<title>Nora Bastevin – Newspaper Ad</title>
<link rel="stylesheet" href="https://fonts.googleapis.com/css2?family=Roboto+Condensed:wght@400;700&display=swap">
<style>
  :root {
    --brand-red: #d9000d;
    --ink: #1f1f1f;
    --paper: #ffffff;
    --badge-black: #000000;
    --badge-edge: #555555;
  }
  * { margin: 0; padding: 0; box-sizing: border-box; }
  html, body { width: 1200px; height: 1169px; overflow: hidden; background: var(--paper); }
  .ad {
    position: relative; width: 1200px; height: 1169px;
    background: var(--paper);
    font-family: "Roboto Condensed", "Arial Narrow", sans-serif;
    color: var(--paper);
  }
  .top-band { position: absolute; left: 0; top: 0; width: 1200px; height: 589px; background: var(--brand-red); }
  .portrait-frame {
    position: absolute; left: 35px; top: 39px; width: 492px; height: 627px;
    background: var(--paper); padding: 7px;
  }
  .portrait {
    width: 100%; height: 100%;
    background: linear-gradient(160deg, #d9d4bf 0%, #b9b390 35%, #e3d6c9 65%, #c8aaa4 100%);
  }
  .headline {
    position: absolute; left: 574px; top: 34px;
    font-weight: 700; font-size: 100px; line-height: 103px; letter-spacing: 4px;
    text-transform: uppercase;
  }
  .agent-name {
    position: absolute; left: 568px; top: 436px;
    font-weight: 700; font-size: 70px; line-height: 72px; text-transform: uppercase;
  }
  .agent-name sup { font-size: 32px; vertical-align: 28px; font-weight: 400; }
  .phone {
    position: absolute; left: 570px; top: 600px;
    display: flex; align-items: center; gap: 18px;
    color: var(--ink); font-size: 70px; line-height: 70px; font-weight: 400;
  }
  .phone svg { width: 60px; height: 60px; }
  .brokerage {
    position: absolute; left: 57px; top: 730px; width: 410px; height: 217px;
    display: flex; flex-direction: column; align-items: center; justify-content: center; gap: 4px;
    color: var(--brand-red); font-weight: 700; text-transform: uppercase; text-align: center;
  }
  .brokerage-name { font-size: 72px; line-height: 72px; }
  .brokerage-sub { font-size: 40px; line-height: 44px; letter-spacing: 2px; }
  .listing-badge {
    position: absolute; left: 541px; top: 730px; width: 615px; height: 215px;
    background: var(--badge-black); border: 2px solid var(--badge-edge);
    padding: 14px;
  }
  .listing-badge-inner {
    width: 100%; height: 100%;
    border: 2px solid var(--paper);
  }
  .bottom-band {
    position: absolute; left: 0; top: 995px; width: 1200px; height: 174px;
    background: var(--brand-red); text-align: center;
  }
  .email {
    display: flex; justify-content: center; align-items: center; gap: 10px;
    margin-top: 16px; font-size: 41px; line-height: 48px;
  }
  .email svg { width: 44px; height: 44px; }
  .tagline { margin-top: 10px; font-weight: 700; font-size: 76px; line-height: 80px; text-transform: uppercase; }
</style>
</head>
<body>
<main class="ad">
  <div class="top-band"></div>

  <div class="portrait-frame">
    <div class="portrait" role="img" aria-label="Portrait photo of agent Nora Bastevin smiling, outdoors"></div>
  </div>

  <h1 class="headline">Buying or<br>Selling<br>Your Home?</h1>

  <p class="agent-name">Nora Bastevin<br>Vestran<sup>®</sup></p>

  <p class="phone">
    <svg viewBox="0 0 60 60" aria-hidden="true">
      <circle cx="30" cy="30" r="30" fill="var(--ink)"/>
      <path d="M25 14h6v10h-5c-1 4-1 8 0 12h5v10h-6c-7-5-7-27 0-32z" fill="var(--paper)"/>
    </svg>
    302-555-0147
  </p>

  <div class="brokerage">
    <span class="brokerage-name">Holloway</span>
    <span class="brokerage-sub">Summit Realty</span>
  </div>

  <div class="listing-badge" aria-hidden="true">
    <div class="listing-badge-inner"></div>
  </div>

  <footer class="bottom-band">
    <p class="email">
      <svg viewBox="0 0 44 44" aria-hidden="true">
        <circle cx="22" cy="22" r="21" fill="var(--paper)"/>
        <rect x="10" y="14" width="24" height="16" fill="none" stroke="var(--brand-red)" stroke-width="2.5"/>
        <path d="M10 14l12 10 12-10M10 30l9-8M34 30l-9-8" fill="none" stroke="var(--brand-red)" stroke-width="2.5"/>
      </svg>
      NoraBastevin@postmail.com
    </p>
    <p class="tagline">Where Home Stories Start</p>
  </footer>
</main>
</body>
</html>
```